Business Card Design Project

I want a design for my business cards based on an excisting logo design.

Target Market(s)

Marketeers, PR-peeps, CEO's, decisionmakers, entrepreneurs

Industry/Entity Type

Business

Requirements
Nice to have
• Some visual interest on the back too
Should not have
• Sarif on the font

```html
<!DOCTYPE html>
<html lang="en">
<head>
<meta charset="utf-8">
<title>LeafLine PR – Business Card</title>
<link rel="stylesheet" href="https://fonts.googleapis.com/css2?family=Ubuntu:wght@400;500&display=swap">
<style>
  :root {
    --backdrop: #2b2b2b;
    --green-light: #a9d13c;
    --green-mid: #92c42a;
    --green-deep: #7fb51e;
    --green-text: #2c9a3c;
    --ink: #555555;
    --ink-soft: #6f6f6f;
    --wordmark: #777777;
    --divider: #d0d0d0;
    --ring: #e6e6e7;
    --paper: #ffffff;
    --icon: #8a8a8a;
  }
  * { box-sizing: border-box; margin: 0; padding: 0; }
  html, body {
    width: 1200px; height: 800px; overflow: hidden;
    background: var(--backdrop);
    font-family: "Ubuntu", sans-serif;
  }
  .stage {
    position: relative; width: 1200px; height: 800px;
  }
  .card {
    position: absolute; top: 246px;
    width: 540px; height: 308px;
    border-radius: 16px; overflow: hidden;
  }
  /* Back side */
  .card--back {
    left: 50px;
    background: radial-gradient(ellipse at 30% 10%, var(--green-deep) 0%, var(--green-light) 45%, var(--green-mid) 100%);
  }
  .back-mark {
    position: absolute; left: 270px; top: 148px;
    transform: translate(-50%, -50%);
    width: 140px; height: 140px; border-radius: 50%;
    background: var(--paper);
  }
  .back-name {
    position: absolute; left: 0; width: 540px; top: 224px;
    text-align: center; font-size: 38px; font-weight: 400;
    color: var(--wordmark); letter-spacing: 1px;
  }
  .back-web {
    position: absolute; left: 496px; top: 154px;
    transform: translate(-50%, -50%) rotate(-90deg);
    font-size: 17px; color: var(--green-text); white-space: nowrap;
  }
  /* Front side */
  .card--front {
    left: 610px;
    background: var(--paper);
  }
  .front-ring {
    position: absolute; left: 230px; top: -118px;
    width: 276px; height: 228px; border-radius: 50%;
    background: var(--ring);
  }
  .front-brand {
    position: absolute; left: 0; width: 270px; top: 100px;
    text-align: center;
  }
  .front-brand .dot {
    display: block; margin: 0 auto 14px;
    width: 78px; height: 78px; border-radius: 50%;
    background: var(--green-mid);
  }
  .front-brand .name {
    font-size: 17px; color: var(--wordmark); letter-spacing: 1px;
  }
  .front-divider {
    position: absolute; left: 270px; top: 85px;
    width: 1px; height: 140px; background: var(--divider);
  }
  .contact {
    position: absolute; right: 22px; top: 106px;
    text-align: right; color: var(--ink-soft); font-size: 13.5px;
    line-height: 17px;
  }
  .contact .person {
    font-weight: 500; color: var(--ink); font-size: 14px; margin-bottom: 24px;
  }
  .socials {
    display: flex; gap: 14px; justify-content: flex-end;
    margin-top: 12px; font-size: 12.5px;
  }
  .socials span::before {
    content: ""; display: inline-block; width: 11px; height: 11px;
    background: var(--icon); margin-right: 4px; vertical-align: -1px;
  }
  .address {
    position: absolute; left: 0; width: 540px; top: 276px;
    text-align: center; color: var(--ink-soft); font-size: 13.5px;
  }
</style>
</head>
<body>
<main class="stage">
  <section class="card card--back" aria-label="Card back">
    <div class="back-mark"></div>
    <div class="back-name">LeafLine PR</div>
    <div class="back-web">www.leaflinepr.nl</div>
  </section>

  <section class="card card--front" aria-label="Card front">
    <div class="front-ring"></div>
    <div class="front-brand">
      <span class="dot"></span>
      <div class="name">LeafLine PR</div>
    </div>
    <div class="front-divider"></div>
    <div class="contact">
      <div class="person">Mara Jansen</div>
      <div>mara.jansen@leaflinepr.nl</div>
      <div>+31(0)6 20583914</div>
      <div class="socials"><span>_leaflinepr</span><span>leaflinepr</span></div>
    </div>
    <div class="address">Lindelaan 42 6711 AB Ede</div>
  </section>
</main>
</body>
</html>
```